Business Cards for Corvantis LLC

We need business cards for a new company called “Corvantis LLC”. This is a technology process improvement company providing a comprehensive assessment of the technology used to run their business. The documentation and review process delivers the visibility and reassurance they need to protect their business and plan for the future. The product is called “Halvorne Ledgerwork”. Our primary target is small-medium size businesses, with the deliverables going to the decision maker. We would like to see the designs use the color blue. Our tag line is GUARD WHAT YOU BUILD · STEER IT WITH CLARITY.

Industry/Entity Type

Business

Contact Information for Business Card

Tag line should be on back of card - it does not have to be upper case.

Requirements
Must have
• Please use information when laying out card:
• Name: Darnell Pruitt
• Title: Partner
• Phone Number: (877)555-0143
• Email: dell@corvantisllc.com
• Website: http://corvantisllc.com

```html
<!DOCTYPE html>
<html lang="en">
<head>
<meta charset="utf-8">
<title>Corvantis LLC — Business Cards</title>
<link rel="stylesheet" href="https://fonts.googleapis.com/css2?family=Montserrat:wght@300;400;600;700&display=swap">
<style>
  :root{
    --page:#e6e7e9;
    --blue:#2c6fb8;
    --blue-mid:#2563aa;
    --blue-deep:#1b4a86;
    --blue-ink:#1e5aa3;
    --grey:#7d7f83;
    --white:#ffffff;
    --paper:#f4f5f7;
  }
  *{box-sizing:border-box;margin:0;padding:0}
  html,body{width:1072px;height:1200px;overflow:hidden}
  body{
    background:var(--page);
    font-family:"Montserrat",Arial,sans-serif;
    display:flex;flex-direction:column;align-items:center;justify-content:center;gap:40px;
  }
  .card{position:relative;width:780px;height:545px;overflow:hidden;box-shadow:0 4px 14px rgba(0,0,0,.18)}
  .card-art{position:absolute;inset:0;width:100%;height:100%}

  /* back */
  .brand-back{
    position:absolute;left:0;right:0;top:250px;text-align:center;color:var(--white);
  }
  .brand-back .brand-name{font-weight:700;font-size:54px;letter-spacing:3px;line-height:1}
  .brand-back .brand-suffix{font-weight:700;font-size:24px;letter-spacing:14px;margin-top:8px;padding-left:14px}
  .tagline{
    position:absolute;left:40px;right:40px;top:424px;height:26px;
    background:var(--blue-deep);color:var(--white);
    font-size:20px;font-weight:400;line-height:26px;padding-left:88px;white-space:nowrap;
  }

  /* front */
  .brand-front{position:absolute;left:38px;top:118px;color:var(--blue-ink);text-align:center;width:270px}
  .brand-front .brand-name{font-weight:700;font-size:34px;letter-spacing:1px;line-height:1}
  .brand-front .brand-suffix{font-weight:700;font-size:16px;letter-spacing:10px;margin-top:6px;padding-left:10px}

  .person{position:absolute;right:38px;top:208px;text-align:right;color:var(--white)}
  .person-name{font-size:33px;font-weight:400;line-height:1}
  .person-title{
    display:inline-block;margin-top:8px;background:var(--blue-deep);
    font-size:17px;padding:2px 10px 2px 60px;
  }
  .contacts{position:absolute;right:30px;top:300px;list-style:none;color:var(--white)}
  .contacts li{display:flex;align-items:center;justify-content:flex-end;gap:14px;height:42px;margin-bottom:28px;font-size:24px;white-space:nowrap}
  .contacts svg{width:42px;height:42px;flex:none}
</style>
</head>
<body>

<section class="card card-back" aria-label="Card back">
  <svg class="card-art" viewBox="0 0 465 325" preserveAspectRatio="none" aria-hidden="true">
    <rect width="465" height="325" fill="var(--blue-deep)"/>
    <rect x="14" y="10" width="440" height="305" fill="var(--blue)"/>
    <rect x="22" y="20" width="422" height="283" fill="none" stroke="var(--blue-deep)" stroke-width="1"/>
    <g fill="var(--blue-deep)">
      <rect x="236" y="3" width="4" height="4"/><rect x="244" y="3" width="4" height="4"/><rect x="252" y="3" width="4" height="4"/>
      <rect x="260" y="3" width="4" height="4"/><rect x="268" y="3" width="4" height="4"/>
      <rect x="150" y="318" width="4" height="4"/><rect x="158" y="318" width="4" height="4"/><rect x="166" y="318" width="4" height="4"/>
      <rect x="174" y="318" width="4" height="4"/><rect x="182" y="318" width="4" height="4"/>
    </g>
    <g fill="var(--blue-mid)" opacity=".6">
      <rect x="456" y="120" width="4" height="4"/><rect x="456" y="128" width="4" height="4"/><rect x="456" y="136" width="4" height="4"/><rect x="456" y="144" width="4" height="4"/>
      <rect x="4" y="170" width="4" height="4"/><rect x="4" y="178" width="4" height="4"/><rect x="4" y="186" width="4" height="4"/>
    </g>
  </svg>
  <div class="brand-back">
    <div class="brand-name">CORVANTIS</div>
    <div class="brand-suffix">LLC</div>
  </div>
  <p class="tagline">Guard what you build · Steer it with clarity.</p>
</section>

<section class="card card-front" aria-label="Card front">
  <svg class="card-art" viewBox="0 0 465 325" preserveAspectRatio="none" aria-hidden="true">
    <rect width="465" height="325" fill="var(--blue)"/>
    <polygon points="0,0 318,0 72,325 0,325" fill="var(--paper)"/>
    <polygon points="318,0 332,0 86,325 72,325" fill="var(--blue-mid)"/>
    <polygon points="336,0 350,0 104,325 90,325" fill="var(--grey)"/>
    <polygon points="350,0 353,0 107,325 104,325" fill="var(--white)"/>
    <rect x="0" y="0" width="465" height="5" fill="var(--blue-deep)"/>
    <rect x="0" y="318" width="465" height="7" fill="var(--blue-deep)"/>
    <rect x="458" y="0" width="7" height="325" fill="var(--blue-deep)"/>
    <g fill="var(--blue-deep)">
      <rect x="2" y="120" width="4" height="4"/><rect x="2" y="128" width="4" height="4"/><rect x="2" y="136" width="4" height="4"/>
      <rect x="2" y="144" width="4" height="4"/><rect x="2" y="152" width="4" height="4"/>
    </g>
  </svg>

  <div class="brand-front">
    <div class="brand-name">CORVANTIS</div>
    <div class="brand-suffix">LLC</div>
  </div>

  <div class="person">
    <p class="person-name">Darnell Pruitt</p>
    <p class="person-title">Partner</p>
  </div>

  <ul class="contacts">
    <li>(877)555-0143
      <svg viewBox="0 0 42 42" aria-hidden="true"><circle cx="21" cy="21" r="20" fill="var(--white)"/>
        <path d="M14 12c1-1 2.5-1 3.2 0l2 3c.6.9.4 2-.4 2.6l-1.4 1c1 2.4 2.8 4.2 5.2 5.2l1-1.4c.6-.8 1.7-1 2.6-.4l3 2c1 .7 1 2.2 0 3.2l-1.6 1.6c-1.2 1.2-3 1.4-4.5.6C17.6 27 14.9 24.3 12.6 19.2c-.8-1.5-.6-3.3.6-4.5z" fill="var(--blue)"/></svg>
    </li>
    <li>dell@corvantisllc.com
      <svg viewBox="0 0 42 42" aria-hidden="true"><circle cx="21" cy="21" r="20" fill="var(--white)"/>
        <rect x="11" y="14" width="20" height="14" rx="1.5" fill="var(--blue)"/>
        <path d="M11.5 15l9.5 7.5 9.5-7.5" fill="none" stroke="var(--white)" stroke-width="1.6"/></svg>
    </li>
    <li>http://corvantisllc.com
      <svg viewBox="0 0 42 42" aria-hidden="true"><circle cx="21" cy="21" r="20" fill="var(--white)"/>
        <g fill="none" stroke="var(--blue)" stroke-width="1.8"><circle cx="21" cy="21" r="10"/><ellipse cx="21" cy="21" rx="4.5" ry="10"/><path d="M11 21h20M13 15.5h16M13 26.5h16"/></g></svg>
    </li>
  </ul>
</section>

</body>
</html>
```